Business card for our large format printing and installation business

We want a professional looking business card for our business. We manufacture and install Signs.

On the back of the card add this info
Large Format Graphics Printing & Installations, Event Graphics, Banners, Posters, Vehicle Fleet Graphics, Boat Wraps, Wall Murals, Decals,Displays,Signs,Plaques,Digital Signs

On the Front of the card add the Tallowfern Signs logo, plus On the back of the card add the Orange Tallowfern Wraps logo. The 2 vector logos are attached to the design brief.

Target Market(s)

Local business owners

Contact Information for Business Card

Colors
f37122
f68d4e
f9ba93

Requirements
Must have
• On the Front of the card add the Tallowfern Signs logo, plus On the back of the card add the Orange Tallowfern Wraps logo. The 2 vector logos are attached to the design brief.

```html
<!DOCTYPE html>
<html lang="en">
<head>
<meta charset="utf-8">
<title>Tallowfern Signs – Business Card</title>
<link href="https://fonts.googleapis.com/css2?family=Arimo:wght@400;700&display=swap" rel="stylesheet">
<style>
  :root {
    --bg: #dcdcdc;
    --black: #050505;
    --brown-dark: #2e211c;
    --brown: #5a3424;
    --orange: #f37122;
    --orange-mid: #f68d4e;
    --orange-light: #f9ba93;
    --logo-yellow: #f7b91d;
    --ink: #1c120d;
  }
  * { margin: 0; padding: 0; box-sizing: border-box; }
  html, body { width: 1200px; height: 807px; overflow: hidden; }
  body {
    background: var(--bg);
    font-family: "Arimo", Arial, sans-serif;
    position: relative;
  }
  .card {
    position: absolute;
    top: 113px;
    width: 350px;
    height: 580px;
    overflow: hidden;
    box-shadow: 0 6px 18px rgba(0,0,0,0.25);
  }
  .card--contact { left: 205px; }
  .card--brand { left: 645px; }

  .contact-panel {
    height: 290px;
    padding: 34px 32px;
    background: linear-gradient(160deg, var(--brown-dark) 0%, var(--brown) 45%, #b2571f 100%);
    color: var(--ink);
  }
  .logo-name {
    font-weight: 700;
    color: var(--logo-yellow);
    font-size: 26px;
    line-height: 1.05;
  }
  .person-name { margin-top: 26px; font-size: 20px; font-weight: 700; }
  .person-role { font-size: 15px; margin-top: 2px; }
  .contact-list { list-style: none; margin-top: 24px; font-size: 13px; }
  .contact-list li { display: flex; align-items: center; gap: 8px; margin-bottom: 6px; }
  .contact-list svg { width: 12px; height: 12px; flex: none; }

  .pattern-panel {
    height: 290px;
    background: var(--black);
    display: flex;
    align-items: center;
    justify-content: center;
  }
  .pattern-area {
    width: 240px;
    height: 220px;
    border-radius: 50%;
    background: radial-gradient(circle, var(--orange) 0%, #8a3f12 55%, var(--black) 75%);
  }

  .card--brand {
    background: linear-gradient(200deg, var(--brown-dark) 0%, var(--brown) 40%, #a84f1c 75%, var(--orange) 100%);
    display: flex;
    align-items: center;
    justify-content: center;
  }
  .brand-fold {
    position: absolute;
    left: 0; right: 0; top: 50%;
    height: 1px;
    background: rgba(0,0,0,0.18);
  }
  .brand-logo {
    position: relative;
    font-weight: 700;
    color: var(--logo-yellow);
    font-size: 44px;
    line-height: 1.05;
    text-align: center;
  }
</style>
</head>
<body>
  <section class="card card--contact">
    <div class="contact-panel">
      <div class="logo-name">Tallowfern<br>Signs</div>
      <p class="person-name">Marlo Quenby</p>
      <p class="person-role">founder&amp;CEO</p>
      <ul class="contact-list">
        <li><svg viewBox="0 0 12 12"><circle cx="6" cy="6" r="6" fill="#1c120d"/><path d="M4 3.5l1 1-0.6 0.8c.4.9 1 1.5 1.9 1.9l.8-.6 1 1-.8.9C5.5 8.2 3.8 6.5 3.4 4.3z" fill="#d9a27e"/></svg>+0100 555 210 347</li>
        <li><svg viewBox="0 0 12 12"><circle cx="6" cy="6" r="6" fill="#1c120d"/><path d="M4 3.5l1 1-0.6 0.8c.4.9 1 1.5 1.9 1.9l.8-.6 1 1-.8.9C5.5 8.2 3.8 6.5 3.4 4.3z" fill="#d9a27e"/></svg>+0100 555 781 902</li>
        <li><svg viewBox="0 0 12 12"><circle cx="6" cy="6" r="6" fill="#1c120d"/><rect x="3" y="4" width="6" height="4" fill="none" stroke="#d9a27e" stroke-width="0.8"/><path d="M3 4l3 2.2L9 4" fill="none" stroke="#d9a27e" stroke-width="0.8"/></svg>info@tallowfern.com</li>
        <li><svg viewBox="0 0 12 12"><circle cx="6" cy="6" r="6" fill="#1c120d"/><circle cx="6" cy="6" r="3" fill="none" stroke="#d9a27e" stroke-width="0.8"/><path d="M3 6h6M6 3v6" stroke="#d9a27e" stroke-width="0.6"/></svg>www.tallowfern.com</li>
      </ul>
    </div>
    <div class="pattern-panel">
      <div class="pattern-area" role="img" aria-label="Decorative pattern of orange dots of varying sizes"></div>
    </div>
  </section>

  <section class="card card--brand">
    <div class="brand-fold"></div>
    <div class="brand-logo">Tallowfern<br>Signs</div>
  </section>
</body>
</html>
```